[Fun Project] Design A Website For A Semi Pro Soccer Team!

DESIGN ONLY! [NO CODING NEEDED]

Hey,

Thanks for looking! Are you ready to design a cool project with us?

This may be a once in a lifetime opportunity to design a website for a Semi Pro Soccer Team. Projects like this don't come along very often! This will be a lot of fun for you!

We need a fresh and exciting website design for a new soccer (or football, depending on where you are) team. You can view the existing site here: http://www.trevmorafc.com/

You can get a sense of the team colors and whatnot from that, but the layout is a little dull. We need something more like this: http://www.bellvanequails.com.

We need something that is visual and exciting, something that will appeal to a sports fan. Ideally, we'd love to work with a designer is a fan of the game, as we think he/she would design something more appealing to the demographic.

Be sure to follow the link below and check out our video:

http://clipdrovo.com/user4417302/review/55820147/3c1f0a7d9e

Thank you and good luck!

Target Market(s)

Soccer/football fans and those interested in becoming fans. More than likely, we're talking males 18-40, but don't want to rule out females.

Industry/Entity Type

Work

Font styles to use
Sans Serif

Colors
faee3e
fbed22
eb1f27
000000
f6f6f6

Requirements
Must have
• Picture/video slider in the top left (see video)
1 home page design and 2 interior page designs
Should not have
• Cluttered
Dull
Lame
Poor Design
And for the love of all the is holy please do not submit us a theme or a template from some website. We are smarter then that and will just remove you from the project....REAL Designers, we got your back and won't even consider crappy stuff....

```html
<!DOCTYPE html>
<html lang="en">
<head>
<meta charset="utf-8">
<title>Trevmora FC</title>
<link rel="stylesheet" href="https://fonts.googleapis.com/css2?family=Open+Sans:wght@400;600;800&family=Roboto:wght@500;700&display=swap">
<style>
  :root{
    --yellow:#fbed22;
    --gold:#faee3e;
    --red:#eb1f27;
    --black:#000000;
    --bar:#141414;
    --light:#f6f6f6;
    --crowd-a:#d8c25e;
    --crowd-b:#b9a04a;
  }
  *{box-sizing:border-box;margin:0;padding:0}
  html,body{width:1200px;height:1000px;overflow:hidden;background:var(--light)}
  .site{position:relative;width:1200px;height:1000px;overflow:hidden;font-family:"Open Sans",Arial,sans-serif}
  .crowd-backdrop{position:absolute;inset:95px 0 0 0;background:linear-gradient(180deg,var(--crowd-a) 0%,#cdb655 50%,var(--crowd-b) 100%)}
  .masthead{position:absolute;left:0;top:0;width:1200px;height:95px;background:var(--bar);border-bottom:2px solid #2a2a2a}
  .brand{position:absolute;left:150px;top:32px;display:flex;align-items:center;gap:10px;font-family:"Open Sans",Arial,sans-serif;font-weight:800;font-size:22px;color:var(--yellow);letter-spacing:.5px}
  .brand-dot{width:16px;height:16px;border-radius:50%;background:var(--red)}
  .main-nav{position:absolute;left:420px;top:36px;display:flex;gap:20px;font-family:"Roboto",Arial,sans-serif;font-weight:700;font-size:15px;color:#fff}
  .main-nav .current{color:var(--yellow)}
  .nav-btn{position:absolute;top:23px;width:50px;height:50px;border-radius:50%;display:flex;align-items:center;justify-content:center}
  .nav-btn.search{left:954px;background:#333}
  .nav-btn.cart{left:1012px;background:var(--yellow)}
  .hero-slider{position:absolute;left:134px;top:144px;width:928px;height:333px;background:linear-gradient(135deg,#2b2b2b 0%,#7a1a1e 40%,#e9e2e2 60%,#3a1012 100%)}
  .slide-arrow{position:absolute;top:291px;width:48px;height:60px;border-radius:6px;background:rgba(246,246,246,.75);color:var(--red);font-family:"Roboto",Arial,sans-serif;font-size:30px;display:flex;align-items:center;justify-content:center}
  .slide-arrow.prev{left:110px}
  .slide-arrow.next{left:1042px}
  .feature-card{position:absolute;width:452px;height:147px;display:flex;background:var(--black)}
  .feature-thumb{position:relative;width:204px;height:100%}
  .play-badge{position:absolute;right:12px;top:8px;width:46px;height:46px;border-radius:50%;background:rgba(210,210,210,.8);border:3px solid #555;display:flex;align-items:center;justify-content:center}
  .feature-copy{padding:10px 8px 0 8px;text-transform:uppercase;font-weight:800;line-height:1.05}
  .feature-title{font-size:27px;color:var(--yellow)}
  .feature-sub{font-size:17px;color:var(--yellow)}
  .feature-red{font-size:17px;color:var(--red);margin-top:2px}
  .feature-text{font-weight:400;font-size:12.5px;color:#fff;line-height:1.25;margin-top:10px}
  .c1{left:134px;top:502px}.c2{left:610px;top:502px}.c3{left:134px;top:672px}.c4{left:610px;top:672px}
  .t1{background:linear-gradient(135deg,#7c8f5a,#c9c2b6 50%,#b23a3e)}
  .t2{background:linear-gradient(135deg,#3a3f7a,#a5723f 50%,#e5c232)}
  .t3{background:linear-gradient(135deg,#5a1012,#c42a2e 55%,#2a2a2a)}
  .t4{background:linear-gradient(135deg,#e0a25a,#8a5a3a 55%,#3a2a20)}
</style>
</head>
<body>
<div class="site">
  <div class="crowd-backdrop" role="img" aria-label="Golden-tinted photo of cheering supporters in the stands"></div>

  <header class="masthead">
    <div class="brand"><span class="brand-dot"></span>TREVMORA FC</div>
    <nav class="main-nav">
      <span class="current">Home</span><span>About</span><span>Shop</span><span>Portfolio</span><span>Blog</span><span>Contacts</span>
    </nav>
    <div class="nav-btn search">
      <svg width="16" height="16" viewBox="0 0 16 16"><circle cx="6.5" cy="6.5" r="4.5" fill="none" stroke="#fff" stroke-width="2"/><line x1="10" y1="10" x2="14" y2="14" stroke="#fff" stroke-width="2.5" stroke-linecap="round"/></svg>
    </div>
    <div class="nav-btn cart">
      <svg width="18" height="16" viewBox="0 0 18 16"><path d="M1 2h3l2 8h9l2-6H5" fill="none" stroke="#111" stroke-width="2"/><circle cx="7" cy="13.5" r="1.5" fill="#111"/><circle cx="14" cy="13.5" r="1.5" fill="#111"/></svg>
    </div>
  </header>

  <div class="hero-slider" role="img" aria-label="Match photo of players in red-and-black and white-and-red kits chasing the ball"></div>
  <div class="slide-arrow prev">&lt;</div>
  <div class="slide-arrow next">&gt;</div>

  <article class="feature-card c1">
    <div class="feature-thumb t1" role="img" aria-label="Photo of a women's league player in a striped kit on the pitch">
      <span class="play-badge"><svg width="18" height="20" viewBox="0 0 18 20"><path d="M2 1l15 9-15 9z" fill="#444"/></svg></span>
    </div>
    <div class="feature-copy">
      <div class="feature-title">10 Exciting</div>
      <div class="feature-sub">Moments of Women</div>
      <div class="feature-red">Soccer League</div>
      <p class="feature-text">Lorem ipsum is simply dummy text of the printing and typesetting industry.</p>
    </div>
  </article>

  <article class="feature-card c2">
    <div class="feature-thumb t2" role="img" aria-label="Portrait photo of a player in a yellow jersey">
      <span class="play-badge"><svg width="18" height="20" viewBox="0 0 18 20"><path d="M2 1l15 9-15 9z" fill="#444"/></svg></span>
    </div>
    <div class="feature-copy">
      <div class="feature-title">Exclusive</div>
      <div class="feature-sub">On Field Interview</div>
      <div class="feature-red">Darío Menck</div>
      <p class="feature-text">Lorem ipsum is simply dummy text of the printing and typesetting industry.</p>
    </div>
  </article>

  <article class="feature-card c3">
    <div class="feature-thumb t3" role="img" aria-label="Photo of a player in a red kit celebrating">
      <span class="play-badge"><svg width="18" height="20" viewBox="0 0 18 20"><path d="M2 1l15 9-15 9z" fill="#444"/></svg></span>
    </div>
    <div class="feature-copy">
      <div class="feature-title">Halvorsen</div>
      <div class="feature-sub">Played for Marlow United</div>
      <div class="feature-red">Thrilling Moments</div>
      <p class="feature-text">Lorem ipsum is simply dummy text of the printing and typesetting industry.</p>
    </div>
  </article>

  <article class="feature-card c4">
    <div class="feature-thumb t4" role="img" aria-label="Photo of a player striking a ball at sunset">
      <span class="play-badge"><svg width="18" height="20" viewBox="0 0 18 20"><path d="M2 1l15 9-15 9z" fill="#444"/></svg></span>
    </div>
    <div class="feature-copy">
      <div class="feature-title">History</div>
      <div class="feature-sub">Of Soccer Leagues</div>
      <div class="feature-red">By Ellis Brant</div>
      <p class="feature-text">Lorem ipsum is simply dummy text of the printing and typesetting industry.</p>
    </div>
  </article>
</div>
</body>
</html>
```